Advertising Portal Needs eBrochure

Hi Crowders! Our advertising portal, which focus on the new launches property, needs an online brochure to promote to potential advertisers the benefits of advertising their projects with us. These advertisers will be mainly real estate developers and agencies.

WHAT WE LOOKING FOR
We do not want over-fanciful designs that makes the content hard to read. The use of illustrations and graphics/symbols related to covered topics are encouraged. The overall design should portrait our advertising efficiency through online and social media means. Our website - www.brightkeyhomes.sg.

For draft purposes, just do up the front page, back page, and few inner pages, preferably to include one illustration chart (either on page 7/8). Size wise probably A5 portrait or landscape, for future printing into a booklet.

WORK COMPLETION AND PAYMENT
The $500 stated here is 50% of the payment. Upon getting a desired draft design, we will need you to work on the full content with slight amendments along the way. Once done, we will be paying the balance $500, and we will need the pdf file as well as the work file.

Let your design juice flow, and hope we can work with you!
Updates

Hi Crowders! Thank you for your submissions. We are closing the project as we've decided on a design. It's a pity we can only select one design, as there are a number of good works. Hope we will have a chance to work together on our upcoming projects. Cheers =)

Target Market(s)

Real estate developers, real estate agencies, and perhaps to an extent, individual property sales agent.

Industry/Entity Type

Advertising

Requirements
Should not have
• We prefer not to have much real people kind of stock images. Try not to use images from our portal as we do not have the ownerships. Instead, you can use stock images of property developments artist impression that gives a similar feel.

```html
<!DOCTYPE html>
<html lang="en">
<head>
<meta charset="utf-8">
<title>BrightKeyHomes.sg – Advertiser eBrochure Spread</title>
<link rel="stylesheet" href="https://fonts.googleapis.com/css2?family=Open+Sans:wght@400;600;700&display=swap">
<style>
  :root {
    --canvas: #f1f2f1;
    --paper-edge: #d8ecd6;
    --paper-white: #ffffff;
    --green: #4caf50;
    --green-deep: #3e9f45;
    --lime: #9acd45;
    --mint-veil: rgba(255, 255, 255, 0.22);
    --ink-dark: #1f3b22;
    --ink-light: #ffffff;
  }

  * { box-sizing: border-box; margin: 0; padding: 0; }

  html, body {
    width: 1200px;
    height: 800px;
    overflow: hidden;
    background: var(--canvas);
    font-family: "Open Sans", Arial, sans-serif;
  }

  .spread {
    position: absolute;
    left: 91px;
    top: 40px;
    width: 1018px;
    height: 720px;
    display: flex;
    box-shadow: 0 10px 30px rgba(0, 0, 0, 0.12);
  }

  .page {
    position: relative;
    width: 509px;
    height: 720px;
    padding: 30px;
  }

  .page--left {
    background: linear-gradient(180deg, var(--paper-white) 0%, var(--paper-white) 55%, var(--paper-edge) 100%);
  }

  .page--right {
    background: var(--paper-edge);
  }

  .panel {
    position: relative;
    width: 100%;
    height: 100%;
    background: var(--green);
    overflow: hidden;
  }

  .panel__decor {
    position: absolute;
    inset: 0;
    width: 100%;
    height: 100%;
  }

  .panel__content {
    position: relative;
    padding: 44px 36px 0 40px;
    color: var(--ink-light);
    font-size: 9.6px;
    line-height: 1.55;
  }

  .section-title {
    font-size: 10.5px;
    font-weight: 700;
    letter-spacing: 0.04em;
    text-transform: uppercase;
    margin: 16px 0 6px;
  }

  .section-title:first-child { margin-top: 0; }

  .panel__content p { margin-bottom: 9px; }

  .closing-note {
    color: var(--ink-dark);
    font-weight: 600;
    font-size: 10.2px;
    margin-top: 14px;
  }

  .step-heading {
    color: var(--ink-dark);
    font-weight: 700;
    font-size: 11px;
    margin-bottom: 4px;
  }

  .step-tag {
    display: inline-block;
    color: var(--ink-dark);
    font-weight: 700;
    font-size: 8.5px;
    letter-spacing: 0.08em;
    text-transform: uppercase;
    margin-bottom: 10px;
  }

  .page-number {
    position: absolute;
    right: 20px;
    bottom: 16px;
    color: var(--ink-light);
    font-size: 8px;
  }
</style>
</head>
<body>
  <main class="spread">
    <section class="page page--left">
      <div class="panel">
        <svg class="panel__decor" viewBox="0 0 449 660" preserveAspectRatio="none" aria-hidden="true">
          <polygon points="300,230 449,230 449,660 120,660" fill="var(--lime)" opacity="0.85"/>
          <polygon points="449,230 449,660 330,660" fill="var(--green-deep)" opacity="0.35"/>
          <polygon points="0,500 240,660 0,660" fill="var(--mint-veil)"/>
        </svg>
        <div class="panel__content">
          <h2 class="section-title">About BrightKeyHomes.sg</h2>
          <p>BrightKeyHomes.sg is a fast growing property search portal, which focuses on the new property developments in the market.</p>
          <p>Working closely with real estate developers and agencies, we provide consumers with genuine, reliable and up-to-date information on the current and new property launches. Together with an interface that is both clean and easy to navigate, BrightKeyHomes.sg will soon become the "go-to" portal for consumers looking for new property launches.</p>

          <h2 class="section-title">How Are We Different</h2>
          <p>When you advertise with BrightKeyHomes.sg, you are not just advertising with us. Instead of simply providing a platform and wait for consumers to take notice of your project, we initiate to reach out to them.</p>
          <p>Together with our team of designated marketing specialists – which includes the very top expertise in Search Engine Optimisation (SEO) &amp; Social Media Marketing, experienced copywriters and innovative designers – we formulate the best package for your project, and work out an integrated marketing campaign at the most effective rates.</p>

          <p class="closing-note">In 3 simple steps, you will see how our service will yield better response, greater results, and stronger awareness for your project, as well as for your company.</p>
        </div>
        <span class="page-number">1</span>
      </div>
    </section>

    <section class="page page--right">
      <div class="panel">
        <svg class="panel__decor" viewBox="0 0 449 660" preserveAspectRatio="none" aria-hidden="true">
          <polygon points="0,0 449,0 449,120 0,190" fill="var(--mint-veil)"/>
          <polygon points="0,0 200,0 0,150" fill="var(--lime)" opacity="0.7"/>
        </svg>
        <div class="panel__content">
          <h1 class="step-heading">1. We Create A Full-Featured Webpage For Your Project</h1>
          <span class="step-tag">Good Deals</span>
          <p>Instead of having your project appear merely like a listing, or by simply linking to your own site, we create a full-featured webpage for your project on our portal – complete with all the essential information, attractive visuals, and clear calls to action that turn visitors into enquiries.</p>
          <p>See an example: http://www.brightkeyhomes.sg/ – each project page is laid out so that potential buyers find every detail at a glance.</p>
          <p>By better presenting your project, we leave potential buyers with a good impression, and a better chance of them to make an enquiry or view the showflat.</p>

          <h2 class="section-title">We Do It All For You</h2>
          <p>If you have any worries on the hassles required to get this done – well, you don't have to. Simply send us all your available information and related files, and our team of writers and designers will put everything together. You can also send us any updates along the way, and we will refresh the webpage accordingly.</p>

          <h2 class="section-title">One Source Of Trusted Information</h2>
          <p>With the many listings on property portals and hundreds of separate websites on each development, it is almost impossible to ensure the right information reaches potential buyers. Working directly with you, we ensure that the details on your project are always accurate and up to date, so buyers receive only genuine information.</p>
          <p>That is why it is important to have one source of trusted information that buyers can rely on. We build that source for you, so your project is presented in the way you prefer, and consumers can make informed decisions with confidence.</p>
          <p>From the project webpage, we will also link back to your company website or official project website for consumers' reference, as well as to promote your company.</p>
        </div>
        <span class="page-number">2</span>
      </div>
    </section>
  </main>
</body>
</html>
```